Apartment Investor Business Card Design

Need a new business card designed for my multifamily investment company

Industry/Entity Type

Real Estate

Contact Information for Business Card

Garrick Pelham - President & CEO
Brightwold Holdings, LLC
4838 North 92nd Avenue, Ste 500
Omaha, NE 68999
(402) 555-0147
Garrick@brightwoldholdings.example
Www.BrightwoldHoldings.example

Colors
3176b5

```html
<!DOCTYPE html>
<html lang="en">
<head>
<meta charset="utf-8">
<title>Brightwold Holdings – Business Card</title>
<link href="https://fonts.googleapis.com/css2?family=Roboto:wght@400;500;700&display=swap" rel="stylesheet">
<style>
  :root {
    --brand-blue: #4f84c8;
    --band-gray: #8e8f92;
    --text-dark: #3f4144;
    --text-mid: #86888b;
    --card-white: #ffffff;
    --card-black: #1c1d1f;
    --page-bg: #e6e7e9;
    --divider: #c9cacc;
  }
  * { margin: 0; padding: 0; box-sizing: border-box; }
  html, body {
    width: 1125px; height: 1200px; overflow: hidden;
    background: var(--page-bg);
    font-family: "Roboto", Arial, sans-serif;
  }
  .card {
    position: absolute; left: 162px; width: 800px; height: 457px;
    box-shadow: 0 4px 12px rgba(0,0,0,0.18);
    overflow: hidden;
  }
  .card--front { top: 95px; background: var(--card-white); }
  .card--back { top: 612px; background: var(--card-black); }

  .brand-name {
    position: absolute; font-weight: 400; letter-spacing: 2px;
    text-transform: uppercase; white-space: nowrap;
  }
  .card--front .brand-name {
    left: 20px; width: 360px; top: 258px; text-align: center;
    font-size: 25px; color: var(--text-dark);
  }
  .card--back .brand-name {
    left: 0; width: 800px; top: 278px; text-align: center;
    font-size: 38px; color: #ffffff;
  }
  .brand-square {
    position: absolute; background: var(--brand-blue);
  }
  .card--front .brand-square { left: 175px; top: 190px; width: 50px; height: 50px; }
  .card--back .brand-square { left: 370px; top: 170px; width: 60px; height: 60px; }

  .divider {
    position: absolute; left: 386px; top: 115px; width: 1px; height: 220px;
    background: var(--divider);
  }
  .contact { position: absolute; left: 415px; top: 116px; color: var(--text-dark); }
  .contact__name { font-size: 29px; font-weight: 700; color: var(--brand-blue); line-height: 1.1; }
  .contact__title { font-size: 19px; font-weight: 500; color: var(--text-mid); margin-top: 2px; }
  .contact__company { font-size: 18px; font-weight: 500; margin-top: 16px; }
  .contact__line { font-size: 18.5px; line-height: 24px; }
  .contact__row { display: flex; align-items: center; gap: 8px; font-size: 18.5px; line-height: 26px; }
  .contact__row:first-of-type { margin-top: 10px; }
  .contact__row svg { width: 18px; height: 18px; fill: var(--brand-blue); }

  .footer-bands { position: absolute; left: 0; bottom: 0; width: 800px; height: 45px; }
  .website {
    position: absolute; right: 32px; bottom: 11px;
    font-size: 18.5px; color: #ffffff;
  }
</style>
</head>
<body>
  <section class="card card--front">
    <div class="brand-square"></div>
    <div class="brand-name">Brightwold Holdings</div>
    <div class="divider"></div>
    <div class="contact">
      <div class="contact__name">Garrick Pelham</div>
      <div class="contact__title">President &amp; CEO</div>
      <div class="contact__company">Brightwold Holdings, LLC</div>
      <div class="contact__line">4838 North 92nd Avenue, Ste 500</div>
      <div class="contact__line">Omaha, NE 68999</div>
      <div class="contact__row">
        <svg viewBox="0 0 24 24" aria-hidden="true"><path d="M6.6 10.8c1.4 2.8 3.8 5.1 6.6 6.6l2.2-2.2c.3-.3.7-.4 1-.2 1.1.4 2.3.6 3.6.6.6 0 1 .4 1 1V20c0 .6-.4 1-1 1C10.6 21 3 13.4 3 4c0-.6.4-1 1-1h3.5c.6 0 1 .4 1 1 0 1.3.2 2.5.6 3.6.1.3 0 .7-.2 1l-2.3 2.2z"/></svg>
        <span>(402) 555-0147</span>
      </div>
      <div class="contact__row">
        <svg viewBox="0 0 24 24" aria-hidden="true"><path d="M2 5h20v14H2V5zm2 2v.5l8 5 8-5V7H4zm0 2.8V17h16V9.8l-8 5-8-5z"/></svg>
        <span>Garrick@brightwoldholdings.example</span>
      </div>
    </div>
    <svg class="footer-bands" viewBox="0 0 800 45" aria-hidden="true">
      <polygon points="0,15 440,15 430,30 0,30" fill="var(--band-gray)"/>
      <rect x="0" y="34" width="800" height="7" fill="var(--brand-blue)"/>
      <polygon points="463,0 800,0 800,45 433,45" fill="var(--brand-blue)"/>
    </svg>
    <div class="website">www.BrightwoldHoldings.example</div>
  </section>

  <section class="card card--back">
    <div class="brand-square"></div>
    <div class="brand-name">Brightwold Holdings</div>
  </section>
</body>
</html>
```